Teacher Grading Software Tri-Fold Brochure Design Project

Design a tri-fold brochure for MarkPilot, a software-as-a-service web application that cuts teacher grading time by 30% to 70%. The purpose of the brochure is to get educators to sign up for a free trial of MarkPilot. In addition to saving teachers valuable time, MarkPilot helps teachers align their teaching with the Unified Benchmark standards, has a built-in rubric generator, and provides students with rubrics along with their assignments. It also provides comment reports that allow educators to see their students' strengths and weaknesses with the push of a button. More information on content is available at MarkPilot's website, www.markpilot-demo.net.
We would like the brochure colors to mesh well with the logo and web site colors (www.markpilot-demo.net).
The design should highlight time and hassle savings, reporting, rubric generation and Unified Benchmark alignment.
Attached are the logo, two images we are willing to provide, if the designer uses them, and some marketing points., Design a tri-fold brochure for MarkPilot, a software-as-a-service web application that cuts teacher grading time by 30% to 70%. The purpose of the brochure is to get educators to sign up for a free trial of MarkPilot. In addition to saving teachers valuable time, MarkPilot helps teachers align their teaching with the Unified Benchmark standards, has a built-in rubric generator, and provides students with rubrics along with their assignments. It also provides comment reports that allow educators to see their students' strengths and weaknesses with the push of a button. More information on content is available at MarkPilot's website, www.markpilot-demo.net.
Attached are the logo, two images we are willing to provide, and some marketing points., Design a tri-fold brochure for MarkPilot, a software-as-a-service web application that cuts teacher grading time by 30% to 70%. The purpose of the brochure is to get educators to sign up for a free trial of MarkPilot. In addition to saving teachers valuable time, MarkPilot helps teachers align their teaching with the Unified Benchmark standards, has a built-in rubric generator, and provides students with rubrics along with their assignments. It also provides comment reports that allow educators to see their students' strengths and weaknesses with the push of a button. More information on content is available at MarkPilot's website, www.markpilot-demo.net.
Attached are the logo, two images we are willing to provide, and some marketing points.
Target Market(s)
School teachers, school principals, school district superintendents
Industry/Entity Type
Marketing
Look and feel

```html
<!DOCTYPE html>
<html lang="en">
<head>
<meta charset="utf-8">
<title>MarkPilot Tri-Fold Brochure</title>
<link rel="stylesheet" href="https://fonts.googleapis.com/css2?family=Open+Sans:ital,wght@0,400;0,600;0,700;1,600&display=swap">
<style>
  :root{
    --teal:#27a88a;
    --teal-dark:#1d8c72;
    --slate:#2b3b45;
    --slate-mid:#4b5d67;
    --red:#df2f2c;
    --ink:#333c42;
    --muted:#555f66;
    --paper:#f7f7f6;
    --paper-edge:#e4e6e6;
    --stage:#ebe8e3;
    --font:'Open Sans', Arial, sans-serif;
  }
  *{box-sizing:border-box;margin:0;padding:0}
  html,body{width:1200px;height:518px;overflow:hidden}
  body{background:var(--stage);font-family:var(--font);color:var(--ink)}

  .sheet{position:absolute;top:42px;width:562px;height:434px;background:linear-gradient(90deg,var(--paper) 0%,#fff 50%,var(--paper) 100%);box-shadow:0 2px 8px rgba(0,0,0,.18);overflow:hidden}
  .sheet--outside{left:28px}
  .sheet--inside{left:610px}
  .sheet__bands{position:absolute;inset:0;width:100%;height:100%}
  .panel{position:absolute;top:0;width:187.33px;height:434px;border-left:1px solid rgba(0,0,0,.06)}
  .panel:nth-of-type(1){left:0;border-left:none}
  .panel:nth-of-type(2){left:187.33px}
  .panel:nth-of-type(3){left:374.66px}

  .photo{position:absolute;border-radius:1px}
  .wordmark{font-weight:700;color:var(--slate);letter-spacing:-.2px;display:inline-flex;align-items:center;gap:3px}
  .wordmark__dot{display:inline-block;width:.42em;height:.42em;border-radius:50%;background:var(--teal)}

  .heading-red{color:var(--red);font-weight:600;font-size:12.5px;line-height:1.1}
  .heading-red .wordmark{font-size:inherit}
  .heading-dark{color:var(--slate);font-weight:700;line-height:1.12}

  .checklist{list-style:none}
  .checklist li{position:relative;padding-left:10px;font-size:6.7px;line-height:1;margin-bottom:6.6px;color:var(--muted)}
  .checklist li::before{content:"";position:absolute;left:0;top:0;width:6px;height:6px;border-radius:50%;background:var(--teal)}
  .checklist li::after{content:"";position:absolute;left:1.8px;top:1.2px;width:1.6px;height:2.8px;border:solid #fff;border-width:0 1px 1px 0;transform:rotate(45deg)}

  .url{display:flex;align-items:center;justify-content:center;gap:3px;font-weight:700;color:var(--red);font-size:9.2px}
  .url__globe{width:8px;height:8px}
  .cta-line{text-align:center;font-weight:700;font-size:7px;color:var(--slate);line-height:1.25}

  .phone{position:absolute;bottom:10px;display:flex;align-items:center;gap:4px;color:#fff;font-weight:700;font-size:8px}
  .phone__icon{width:9px;height:9px}

  /* outside */
  .try-today{position:absolute;left:22px;top:52px}
  .try-today .checklist{margin-top:9px}
  .trial-box{position:absolute;left:0;width:100%;top:158px}
  .trial-box .url{margin-top:5px}
  .photo--students{left:22px;top:206px;width:150px;height:148px;border-radius:50% 50% 45% 45%;background:radial-gradient(ellipse at 50% 45%,#d9a98a 0%,#c57d5f 35%,#9db7cf 65%,rgba(200,200,200,0) 72%)}
  .photo--relaxing{left:16px;top:66px;width:154px;height:140px;background:linear-gradient(180deg,#f0f0f0 0%,#e7e7e8 40%,#2d3440 55%,#232933 80%,#dcdcdc 100%)}
  .love{position:absolute;left:22px;top:246px}
  .love .checklist{margin-top:10px}
  .visit{position:absolute;left:0;width:100%;top:356px;text-align:center}
  .visit .url{margin:4px 0}
  .cover-logo{position:absolute;left:0;width:100%;top:78px;text-align:center}
  .cover-logo .wordmark{font-size:27px}
  .tagline{position:absolute;left:22px;right:22px;top:122px;text-align:center;font-style:italic;font-weight:600;font-size:14.5px;line-height:18.5px;color:var(--slate-mid)}
  .photo--papers{left:24px;top:244px;width:140px;height:120px;background:linear-gradient(180deg,#f4f4f2 0%,#e1dfd9 50%,#c9c6bf 100%)}
  .cover-url{position:absolute;bottom:10px;left:0;width:100%;display:flex;justify-content:center;align-items:center;gap:3px;color:#fff;font-size:8px;font-weight:600}

  /* inside */
  .photo--tablet{left:84px;top:10px;width:103px;height:122px;background:linear-gradient(160deg,#efe7df 0%,#d9c4b0 40%,#b48a6a 60%,#e8e2dc 100%)}
  .inside-logo{position:absolute;left:22px;top:60px}
  .inside-logo .wordmark{font-size:10px}
  .how{position:absolute;left:22px;top:102px;width:60px;font-size:14px}
  .steps{position:absolute;left:12px;right:10px;top:146px;list-style:none}
  .steps li{position:relative;padding-left:9px;font-size:5.2px;line-height:1.3;margin-bottom:4.6px;color:var(--muted)}
  .steps li::before{content:"";position:absolute;left:0;top:.5px;width:2px;height:4px;border:solid var(--red);border-width:0 1.3px 1.3px 0;transform:rotate(40deg)}

  .cta{position:absolute;left:0;width:100%;text-align:center}
  .cta .heading-red{font-size:11.5px}
  .cta .url{font-size:8px;margin-top:2px}

  .does{position:absolute;left:16px;top:24px;font-size:14.5px}
  .features{position:absolute;left:16px;right:10px;top:64px;list-style:none}
  .features li{margin-bottom:7px}
  .feature__title{position:relative;padding-left:10px;font-size:8px;font-weight:700;color:var(--red);line-height:1.1}
  .feature__title::before{content:"";position:absolute;left:0;top:1.5px;width:6px;height:6px;border-radius:50%;background:radial-gradient(circle at 35% 35%,#8fd9b8,var(--teal) 60%)}
  .feature__text{font-size:5.3px;line-height:1.32;color:var(--muted);margin-top:2.5px}

  .secure{position:absolute;left:16px;right:12px;top:40px}
  .other{position:absolute;left:16px;top:108px;font-size:14.5px}
  .more-features{position:absolute;left:16px;right:12px;top:138px;list-style:none}
  .more-features li{position:relative;padding-left:9px;font-size:5.3px;line-height:1.32;color:var(--muted);margin-bottom:6px}
  .more-features li::before{content:"";position:absolute;left:0;top:.5px;width:5px;height:5px;border-radius:50%;border:.8px solid var(--red)}
  .more-features li::after{content:"";position:absolute;left:1.6px;top:2px;width:0;height:0;border-left:2px solid var(--red);border-top:1.1px solid transparent;border-bottom:1.1px solid transparent}
  .photo--relaxed{left:10px;top:326px;width:170px;height:80px;background:linear-gradient(180deg,#f4f5f6 0%,#e3e6e8 45%,#6b4a3a 60%,#f2f2f2 100%)}
  .photo-logo{position:absolute;left:18px;top:332px}
  .photo-logo .wordmark{font-size:10px}
</style>
</head>
<body>

<section class="sheet sheet--outside" aria-label="Brochure outside">
  <svg class="sheet__bands" viewBox="0 0 562 434" preserveAspectRatio="none" aria-hidden="true">
    <defs>
      <linearGradient id="slateFade" x1="0" y1="0" x2="0" y2="1">
        <stop offset="0" stop-color="#24333d"/><stop offset="1" stop-color="#5a6b74"/>
      </linearGradient>
    </defs>
    <path d="M0 0H562V30C470 6 360 36 250 14C180 2 90 14 0 20Z" fill="url(#slateFade)"/>
    <path d="M0 24C90 18 160 10 240 26C300 38 250 30 230 28C150 20 80 28 0 30Z" fill="var(--red)"/>
    <path d="M374 34C430 22 500 18 562 26V30C500 24 440 28 374 38Z" fill="var(--red)"/>
    <path d="M0 434V362C60 382 140 412 220 434Z" fill="url(#slateFade)"/>
    <path d="M0 352C70 372 150 408 232 432L222 434C140 412 60 382 0 360Z" fill="var(--red)"/>
    <path d="M240 434C340 422 450 404 562 386V434Z" fill="var(--teal)"/>
    <path d="M374 406C440 392 500 380 562 372V378C500 386 440 398 374 410Z" fill="#9aa6ac"/>
    <path d="M374 396C450 380 510 370 562 366V368C510 374 450 384 374 400Z" fill="var(--red)"/>
  </svg>

  <div class="panel">
    <div class="try-today">
      <h2 class="heading-red">Try <span class="wordmark">MarkPilot</span> Today</h2>
      <ul class="checklist">
        <li>Save your time</li>
        <li>Eliminate most paper-handling</li>
        <li>Standardize grading comments</li>
        <li>Standardize rubrics</li>
        <li>Embrace Unified Benchmark standards</li>
        <li>Get real-time performance data</li>
      </ul>
    </div>
    <div class="trial-box">
      <p class="cta-line">Start a Risk-Free<br>Full-Function Trial Today At:</p>
      <p class="url"><svg class="url__globe" viewBox="0 0 10 10" aria-hidden="true"><circle cx="5" cy="5" r="4.3" fill="none" stroke="#556" stroke-width=".9"/><ellipse cx="5" cy="5" rx="1.8" ry="4.3" fill="none" stroke="#556" stroke-width=".7"/><path d="M.8 5H9.2" stroke="#556" stroke-width=".7"/></svg>www.markpilot-demo.net</p>
    </div>
    <div class="photo photo--students" role="img" aria-label="Photo of a cheerful group of students giving thumbs up"></div>
    <p class="phone" style="left:22px"><svg class="phone__icon" viewBox="0 0 10 10" aria-hidden="true"><circle cx="5" cy="5" r="4.5" fill="var(--teal)"/><path d="M3.4 2.6l1 1-.6.8c.3.7.8 1.2 1.5 1.5l.8-.6 1 1-.7.9C4.6 7 3 5.4 2.7 3.3Z" fill="#fff"/></svg>800-555-0147</p>
  </div>

  <div class="panel">
    <div class="photo photo--relaxing" role="img" aria-label="Photo of a relaxed teacher leaning back with hands behind his head"></div>
    <div class="love">
      <h2 class="heading-red">You'll Love <span class="wordmark">MarkPilot</span></h2>
      <ul class="checklist">
        <li>Teachers love saving time and hassle</li>
        <li>Students love how easy it is to use</li>
        <li>Administrators love the statistics</li>
        <li>Everyone loves the standardization</li>
        <li>Mother Earth loves saving trees</li>
      </ul>
    </div>
    <div class="visit">
      <p class="cta-line">Visit</p>
      <p class="url"><svg class="url__globe" viewBox="0 0 10 10" aria-hidden="true"><circle cx="5" cy="5" r="4.3" fill="none" stroke="#556" stroke-width=".9"/><ellipse cx="5" cy="5" rx="1.8" ry="4.3" fill="none" stroke="#556" stroke-width=".7"/><path d="M.8 5H9.2" stroke="#556" stroke-width=".7"/></svg>www.markpilot-demo.net</p>
      <p class="cta-line">to start your free trial today</p>
    </div>
  </div>

  <div class="panel">
    <div class="cover-logo"><span class="wordmark">MarkPilot<span class="wordmark__dot"></span></span></div>
    <p class="tagline">An affordable, web-based grading application that saves educators hundreds of hours per year</p>
    <div class="photo photo--papers" role="img" aria-label="Photo of a tall stack of paper assignments"></div>
    <p class="cover-url"><svg class="url__globe" viewBox="0 0 10 10" aria-hidden="true"><circle cx="5" cy="5" r="4.3" fill="#e05a3a"/></svg>www.markpilot-demo.net</p>
  </div>
</section>

<section class="sheet sheet--inside" aria-label="Brochure inside">
  <svg class="sheet__bands" viewBox="0 0 562 434" preserveAspectRatio="none" aria-hidden="true">
    <defs>
      <linearGradient id="slateFadeIn" x1="0" y1="0" x2="0" y2="1">
        <stop offset="0" stop-color="#24333d"/><stop offset="1" stop-color="#5a6b74"/>
      </linearGradient>
    </defs>
    <path d="M0 0H190C150 12 90 26 0 44Z" fill="var(--teal)"/>
    <path d="M0 48C90 30 150 18 200 8L202 12C150 22 90 36 0 54Z" fill="var(--red)"/>
    <path d="M190 0H562V24C470 8 320 4 190 8Z" fill="var(--teal)"/>
    <path d="M374 0H562V40C510 24 450 14 374 10Z" fill="url(#slateFadeIn)"/>
    <path d="M0 434V400C60 410 120 422 176 434Z" fill="url(#slateFadeIn)"/>
    <path d="M0 392C70 402 140 418 196 434H184C128 422 60 408 0 400Z" fill="var(--red)"/>
    <path d="M190 434C300 424 420 420 562 418V434Z" fill="var(--teal)"/>
    <path d="M374 434C440 420 500 400 562 380V434Z" fill="var(--teal)"/>
    <path d="M374 418C440 402 500 386 562 372V378C500 392 440 410 374 424Z" fill="var(--red)"/>
  </svg>

  <div class="panel">
    <div class="photo photo--tablet" role="img" aria-label="Photo of a smiling teacher holding a tablet"></div>
    <div class="inside-logo"><span class="wordmark">MarkPilot</span></div>
    <h2 class="heading-dark how">How it works:</h2>
    <ol class="steps">
      <li>Teachers get a MarkPilot account, available for a free trial at MarkPilot.com. Teachers either get an individual account or join a group, such as a school or district.</li>
      <li>Students create free student accounts.</li>
      <li>Teachers create individual classes by entering the class name and a password the teacher creates. The class will be assigned an ID the students use with the password to sign in to the class.</li>
      <li>Teachers prepare an assignment and enter it into a class with a due date.</li>
      <li>Students in the class use the class ID and password to log in and pick up the assignment.</li>
      <li>Students complete the assignment and upload it to MarkPilot.</li>
      <li>Teachers pick up assignments and grade them using simple point and click. Teachers grade the assignments using MarkPilot's Unified Benchmark-aligned grading comments, the teacher's personal comments and the optional assignment rubric.</li>
      <li>Once the grading is done the work is returned to the student through MarkPilot, with all the comments. A copy of the work is retained for both the student and the teacher.</li>
      <li>The teacher then runs reports that point out class and student areas that show particular competency as well as areas that need more work.</li>
    </ol>
    <div class="cta" style="top:366px">
      <p class="heading-red">Try <span class="wordmark">MarkPilot</span> risk-free at</p>
      <p class="url"><svg class="url__globe" viewBox="0 0 10 10" aria-hidden="true"><circle cx="5" cy="5" r="4.3" fill="none" stroke="#556" stroke-width=".9"/><ellipse cx="5" cy="5" rx="1.8" ry="4.3" fill="none" stroke="#556" stroke-width=".7"/><path d="M.8 5H9.2" stroke="#556" stroke-width=".7"/></svg>www.markpilot-demo.net</p>
    </div>
    <p class="phone" style="left:18px"><svg class="phone__icon" viewBox="0 0 10 10" aria-hidden="true"><circle cx="5" cy="5" r="4.5" fill="var(--red)"/><path d="M3.4 2.6l1 1-.6.8c.3.7.8 1.2 1.5 1.5l.8-.6 1 1-.7.9C4.6 7 3 5.4 2.7 3.3Z" fill="#fff"/></svg>800-555-0147</p>
  </div>

  <div class="panel">
    <h2 class="heading-dark does">What <span class="wordmark">MarkPilot</span><br>Does For You:</h2>
    <ul class="features">
      <li><p class="feature__title">Saves Your Time:</p><p class="feature__text">MarkPilot cuts paper handling and grading time by 30% to 70%!</p></li>
      <li><p class="feature__title">Aligns Grading With Unified Benchmark:</p><p class="feature__text">Over fifty predefined comments provide Unified Benchmark-aligned compliments and constructive criticisms.</p></li>
      <li><p class="feature__title">Enhances Data-Driven Instruction:</p><p class="feature__text">Gives immediate real-time, real-world feedback on student performance. Create one-click reports on comment usage by assignment, class, or student, instantly highlight strengths and weaknesses.</p></li>
      <li><p class="feature__title">Standardizes grading:</p><p class="feature__text">Comment on students' most common mistakes with the simple click of a button. Personalize comments quickly and easily. Provide more detailed and meaningful feedback in less time.</p></li>
      <li><p class="feature__title">Manages and Shares Rubrics:</p><p class="feature__text">Create and run reports on narrative rubrics. Rubrics are automatically shared with group members, making department-wide rubric standardization a snap.</p></li>
      <li><p class="feature__title">Manages Revisions:</p><p class="feature__text">Simplify the Unified Benchmark-mandated revision process by tracking revisions as they are uploaded. Make revisions visible to students and comment on each version individually.</p></li>
      <li><p class="feature__title">Manages Schedules:</p><p class="feature__text">Notify students of assignments, get notified if an assignment is late and send deadline reminders to students.</p></li>
      <li><p class="feature__title">Brings Groups Together:</p><p class="feature__text">MarkPilot is designed to be used by teachers and larger groups. Groups can run comment usage reports by class, teacher or group. Know which techniques and instructors are most effective and make data-driven curriculum development far easier.</p></li>
    </ul>
    <div class="cta" style="top:384px">
      <p class="heading-red">Try <span class="wordmark">MarkPilot</span> risk-free at</p>
      <p class="url"><svg class="url__globe" viewBox="0 0 10 10" aria-hidden="true"><circle cx="5" cy="5" r="4.3" fill="none" stroke="#556" stroke-width=".9"/><ellipse cx="5" cy="5" rx="1.8" ry="4.3" fill="none" stroke="#556" stroke-width=".7"/><path d="M.8 5H9.2" stroke="#556" stroke-width=".7"/></svg>www.markpilot-demo.net</p>
    </div>
  </div>

  <div class="panel">
    <div class="secure">
      <p class="feature__title">Can Be Securely Used Anywhere:</p>
      <p class="feature__text">Entirely web-based so there is no need to carry around and track large piles of paper. Uses the latest encryption technologies to ensure student confidentiality. Grade anywhere on nearly any device, including desktops, laptops, tablets and smartphones.</p>
    </div>
    <h2 class="heading-dark other">Other Features:</h2>
    <ul class="more-features">
      <li>Reporting can be done on a student, class, teacher or group level.</li>
      <li>Student assignments can be revised any number of times up until the due date.</li>
      <li>The teacher's dashboard shows the status of all assignments and gives the teacher the ability to drill down into details of each student and assignment.</li>
      <li>Complete portfolios are maintained in MarkPilot, with all student submissions and grades kept in a secure database.</li>
      <li>Teachers can share common, standardized rubrics with their peers.</li>
    </ul>
    <div class="cta" style="top:264px">
      <p class="heading-red">Try <span class="wordmark">MarkPilot</span> risk-free at</p>
      <p class="url"><svg class="url__globe" viewBox="0 0 10 10" aria-hidden="true"><circle cx="5" cy="5" r="4.3" fill="none" stroke="#556" stroke-width=".9"/><ellipse cx="5" cy="5" rx="1.8" ry="4.3" fill="none" stroke="#556" stroke-width=".7"/><path d="M.8 5H9.2" stroke="#556" stroke-width=".7"/></svg>www.markpilot-demo.net</p>
    </div>
    <div class="photo photo--relaxed" role="img" aria-label="Photo of a happy teacher relaxing with hands behind her head"></div>
    <div class="photo-logo"><span class="wordmark">MarkPilot</span></div>
    <p class="phone" style="right:12px"><svg class="phone__icon" viewBox="0 0 10 10" aria-hidden="true"><circle cx="5" cy="5" r="4.5" fill="#fff"/><path d="M3.4 2.6l1 1-.6.8c.3.7.8 1.2 1.5 1.5l.8-.6 1 1-.7.9C4.6 7 3 5.4 2.7 3.3Z" fill="var(--teal)"/></svg>800-555-0147</p>
  </div>
</section>

</body>
</html>
```